Business Card for TQB Field Services

Would like a large logo on one side. On the other side, logo on one side and company phone number, address, and email on the other side. I don't have a logo so please create one for us.
Updates
I don't have a logo, so please create one for us.
Target Market(s)
Land Surveying
Industry/Entity Type
Surveyor
Contact Information for Business Card
Would like a large logo on one side. On the other side, logo on one side and company phone number, address, and email on the other side
Requirements
Nice to have
- would like the initials to be incorporated with the logo

```html
<!DOCTYPE html>
<html lang="en">
<head>
<meta charset="UTF-8">
<title>TQB Field Services – Business Card</title>
<link rel="stylesheet" href="https://fonts.googleapis.com/css2?family=Open+Sans:wght@400;800&display=swap">
<style>
  :root {
    --navy: #26226a;
    --grey: #6d6e71;
    --paper: #ffffff;
    --ink: #3a3a3c;
    --backdrop: #e4e4e6;
  }
  * { box-sizing: border-box; margin: 0; padding: 0; }
  html, body { width: 1200px; height: 1200px; overflow: hidden; }
  body {
    background: var(--backdrop);
    font-family: "Open Sans", Arial, sans-serif;
    position: relative;
  }
  .card {
    position: absolute;
    left: 198px;
    width: 804px;
    height: 456px;
    overflow: hidden;
    box-shadow: 0 4px 14px rgba(0,0,0,0.25);
  }
  .card-front { top: 98px; background: var(--navy); color: var(--paper); }
  .card-back { top: 645px; background: var(--paper); }

  .wordmark { font-weight: 800; line-height: 1; }
  .wordmark .initials { display: block; letter-spacing: 2px; }
  .wordmark .tagline { display: block; letter-spacing: 1px; }

  .card-front .wordmark {
    position: absolute;
    left: 0; right: 0; top: 138px;
    text-align: center;
    color: var(--paper);
  }
  .card-front .initials { font-size: 118px; }
  .card-front .tagline { font-size: 44px; margin-top: 8px; }
  .website {
    position: absolute;
    left: 0; right: 0; top: 406px;
    text-align: center;
    font-size: 18px;
  }

  .card-back .wordmark {
    position: absolute;
    left: 52px; top: 46px;
    color: var(--navy);
  }
  .card-back .initials { font-size: 104px; }
  .card-back .tagline { font-size: 38px; margin-top: 6px; }

  .person {
    position: absolute;
    right: 42px; top: 198px;
    text-align: right;
  }
  .person-name { font-size: 29px; color: var(--navy); line-height: 1.2; }
  .person-title { font-size: 19px; color: var(--ink); }
  .accent-bar {
    position: absolute;
    left: 789px; top: 203px;
    width: 15px; height: 58px;
    background: var(--navy);
  }
  .address {
    position: absolute;
    left: 52px; top: 276px;
    font-size: 20px; color: var(--ink);
  }
  .contact-list {
    position: absolute;
    left: 50px; top: 312px;
    list-style: none;
    font-size: 20px; color: var(--ink);
  }
  .contact-list li { display: flex; align-items: center; height: 27px; }
  .contact-list svg { width: 17px; height: 17px; margin-right: 8px; fill: var(--navy); }
  .wave { position: absolute; left: 0; top: 0; }
</style>
</head>
<body>
  <section class="card card-front">
    <div class="wordmark">
      <span class="initials">TQB</span>
      <span class="tagline">FIELD SERVICES</span>
    </div>
    <p class="website">www.TQBllc.com</p>
  </section>

  <section class="card card-back">
    <svg class="wave" width="804" height="456" viewBox="0 0 804 456" aria-hidden="true">
      <path d="M234,420 C420,385 600,352 804,352 L804,372 C640,368 470,388 234,420Z" fill="var(--grey)"/>
      <path d="M0,419 C150,432 300,428 480,405 C620,388 720,382 804,384 L804,456 L0,456Z" fill="var(--navy)"/>
    </svg>
    <div class="wordmark">
      <span class="initials">TQB</span>
      <span class="tagline">FIELD SERVICES</span>
    </div>
    <div class="person">
      <p class="person-name">Alex Morgan</p>
      <p class="person-title">Managing Partner</p>
    </div>
    <div class="accent-bar"></div>
    <p class="address">456 Meadow Lane, Brookfield, RI 02870</p>
    <ul class="contact-list">
      <li><svg viewBox="0 0 16 16" aria-label="Phone"><path d="M1 5c0-2 3-3 7-3s7 1 7 3v1h-4V4.5H5V6H1zM4 7h8l2 7H2zM8 8.5a2 2 0 1 0 0 4a2 2 0 1 0 0-4z"/></svg>000.000.0000</li>
      <li><svg viewBox="0 0 16 16" aria-label="Mobile"><path d="M4 1h8v14H4zM5.5 3v9h5V3zM7 13h2v1H7z" fill-rule="evenodd"/></svg>000.000.0000</li>
      <li><svg viewBox="0 0 16 16" aria-label="Email"><path d="M1 3h14v10H1zM2.5 4.5v7.2L6 8zM3.5 4.5 8 9l4.5-4.5zM13.5 4.5 10 8l3.5 3.7zM7 9l-3.5 3h9L9 9l-1 1z" fill-rule="evenodd"/></svg>info@tqbllc.com</li>
    </ul>
  </section>
</body>
</html>
```